Occupational Therapist does home accessibility for disabled folks; needs business card design

We need a business card for a company in Portland, Oregon that specializes in making homes accessible, comfortable, and functional for people who are disabled or aging who would like to stay in THEIR home. Our medical background as Occupational Therapists allows us to translate the functional needs of the person into the recommendations for the design of the home remodel.

Target Market(s)

Elderly, children of elderly
People with disabilities, families of people with disabilities

Industry/Entity Type

Business

Contact Information for Business Card

Company name: HomeWise
Name: Danielle Reyes Crawford, OTR/L, CAPS, ECHM
Occupational Therapist, Home Modification & Accessibility Specialist
website: www.homewiseforyears.com
email: homewiseforyears@nestmail.example
phone: (503)218-4057
CCB #: 487315

Font styles to use
Sans Serif

Requirements
Must have
• My logo
• Easy to read font with contrasting background
• Please list the Services offered: Occupational Therapy, Home safety & accessibility assessments, Home modification consulting, project management
Nice to have
• Friendly, welcoming feel
Should not have
• Dark colored background

```html
<!DOCTYPE html>
<html lang="en">
<head>
<meta charset="utf-8">
<title>HomeWise Business Card</title>
<link href="https://fonts.googleapis.com/css2?family=Arimo:wght@400;700&display=swap" rel="stylesheet">
<style>
  :root {
    --orange: #d07d29;
    --grey: #5f5f5f;
    --grey-dark: #4a4a4a;
    --ink: #3d3d3d;
    --white: #ffffff;
    --backdrop: #e6e4e0;
  }
  * { box-sizing: border-box; margin: 0; padding: 0; }
  html, body { width: 1200px; height: 900px; overflow: hidden; }
  body {
    background: var(--backdrop);
    font-family: "Arimo", Arial, sans-serif;
    color: var(--ink);
    display: flex;
    flex-direction: column;
    align-items: center;
    justify-content: center;
    gap: 40px;
  }
  .card {
    position: relative;
    width: 700px;
    height: 400px;
    background: var(--white);
    overflow: hidden;
    box-shadow: 0 6px 18px rgba(0,0,0,0.18);
  }

  /* Brand side */
  .brand-mark {
    position: absolute;
    background: var(--orange);
    color: var(--white);
    font-weight: 700;
    display: flex;
    align-items: center;
    justify-content: center;
    letter-spacing: -1px;
  }
  .card--brand .brand-mark {
    left: 300px; top: 110px; width: 300px; height: 120px;
    font-size: 58px;
  }
  .services {
    position: absolute;
    left: 150px; top: 245px;
    font-size: 15px;
    line-height: 1.45;
    color: var(--ink);
  }
  .services .second { padding-left: 18px; }
  .brand-footer {
    position: absolute;
    left: 0; right: 0; bottom: 0;
    height: 44px;
    background: var(--grey);
    border-top: 5px solid var(--orange);
  }

  /* Contact side */
  .license {
    position: absolute;
    left: 34px; top: 26px;
    font-size: 12px;
    color: var(--orange);
  }
  .contact-band {
    position: absolute;
    left: 0; right: 0; bottom: 0;
    height: 170px;
    background: var(--grey);
  }
  .card--contact .brand-mark {
    left: 34px; top: 140px; width: 260px; height: 130px;
    font-size: 50px;
  }
  .person {
    position: absolute;
    right: 34px; top: 52px;
    text-align: right;
  }
  .person-name {
    font-size: 25px;
    font-weight: 700;
    letter-spacing: 0.5px;
    color: var(--ink);
  }
  .person-name .surname { color: var(--orange); }
  .credentials {
    font-size: 15px;
    font-weight: 700;
    margin-top: 6px;
  }
  .role {
    font-size: 15px;
    line-height: 1.4;
    margin-top: 12px;
  }
  .contact-list {
    position: absolute;
    left: 320px; top: 250px;
    list-style: none;
    color: var(--white);
    font-size: 19px;
    line-height: 1.6;
  }
  .contact-list li { display: flex; align-items: center; gap: 12px; }
  .contact-list svg { width: 18px; height: 18px; flex: none; }
</style>
</head>
<body>

  <section class="card card--brand">
    <div class="brand-mark">HomeWise</div>
    <p class="services">
      Occupational Therapy | Home safety &amp; accessibility assessments<br>
      <span class="second">Home modification consulting | Project management</span>
    </p>
    <div class="brand-footer"></div>
  </section>

  <section class="card card--contact">
    <p class="license">CCB-487315</p>
    <div class="contact-band"></div>
    <div class="brand-mark">HomeWise</div>
    <div class="person">
      <h1 class="person-name">DANIELLE <span class="surname">REYES CRAWFORD</span></h1>
      <p class="credentials">OTR/L,CAPS,ECHM</p>
      <p class="role">Occupational Therapist,Home<br>Modification &amp; Accessibility Specialist</p>
    </div>
    <ul class="contact-list">
      <li>
        <svg viewBox="0 0 20 20" aria-hidden="true"><path fill="var(--orange)" d="M4 2h4l1.5 4-2.2 1.6a11 11 0 0 0 5.1 5.1L14 10.5l4 1.5v4a2 2 0 0 1-2 2A14 14 0 0 1 2 4a2 2 0 0 1 2-2z"/></svg>
        (503)218-4057
      </li>
      <li>
        <svg viewBox="0 0 20 20" aria-hidden="true"><rect x="1" y="4" width="18" height="12" fill="var(--orange)"/><path d="M1 4l9 7 9-7" fill="none" stroke="var(--grey)" stroke-width="1.6"/></svg>
        homewiseforyears@nestmail.example
      </li>
      <li>
        <svg viewBox="0 0 20 20" aria-hidden="true"><circle cx="10" cy="10" r="9" fill="var(--orange)"/><path d="M1 10h18M10 1v18M4 4.5c4 2 8 2 12 0M4 15.5c4-2 8-2 12 0" fill="none" stroke="var(--grey)" stroke-width="1.2"/></svg>
        www.homewiseforyears.com
      </li>
    </ul>
  </section>

</body>
</html>
```